Book cover needed for a major new book on emotional resilience

The book will be titled: 'Storm to Stillness: from rigid habits to pioneers of renewal - The handbook for building steady teams and institutions'
My websites are http://www.brightmarrow.com and http://www.hollenquay.org and I am http://en.pedialoom.org/wiki/Tomas_Brenhurst_(uncertainty_scholar) ad expert in developing emotional resilience. My previous book was The Quiet Compass.
The premise of the book is to introduce brand new material which is the first ever methodology and strategy on how to develop emotional resilience across entire populations like organisations and companies or moving people from fear about change to finding flow through resilience.
The final design should communicate the fact that this is a strategy and methodology. That it is about developing people and entire organisations to be more resilient and who are able to deal with change better.
Target Market(s)
Consultants, Organisational development consultants, Human Resource professionals.

```html
<!DOCTYPE html>
<html lang="en">
<head>
<meta charset="utf-8">
<title>Storm to Stillness – Book Cover</title>
<link href="https://fonts.googleapis.com/css2?family=Anton&family=Roboto:wght@700;900&display=swap" rel="stylesheet">
<style>
  :root {
    --page-bg: #eceded;
    --cover-blue: #6e95cf;
    --cover-blue-dark: #5f86c0;
    --ink: #141414;
    --outline: #ffffff;
    --box-grey: #d9d9d9;
    --sky-top: #7fa6d8;
    --sky-mid: #dfe8f2;
    --rock: #8a8580;
    --rock-dark: #4e4843;
  }
  * { margin: 0; padding: 0; box-sizing: border-box; }
  html, body { width: 1200px; height: 800px; overflow: hidden; background: var(--page-bg); }
  .wrap {
    position: absolute; left: 178px; top: 100px;
    display: flex; width: 844px; height: 600px;
    box-shadow: 0 10px 30px rgba(0,0,0,.18);
  }

  /* Back cover */
  .back-cover {
    width: 400px; height: 600px; background: var(--cover-blue);
    padding: 28px 26px 0; position: relative;
    font-family: "Roboto", Arial, sans-serif; color: var(--ink);
  }
  .back-cover .author { text-align: right; font-weight: 900; font-size: 12px; letter-spacing: .2px; }
  .back-cover .title {
    font-family: "Anton", Impact, sans-serif; font-size: 46px; line-height: 1.05;
    text-align: center; letter-spacing: .5px; margin-top: 2px;
  }
  .back-cover .subtitle { text-align: center; font-weight: 900; font-size: 11px; margin-top: 4px; }
  .back-cover .blurb {
    margin: 24px 10px 0; font-weight: 700; font-size: 10.3px; line-height: 1.42;
    text-align: justify; color: #1d2230;
  }
  .back-cover .placeholder {
    position: absolute; bottom: 30px; width: 92px; height: 38px;
    background: var(--box-grey); display: flex; align-items: center; justify-content: center;
    font-weight: 700; font-size: 10px; color: #2a2a2a;
  }
  .placeholder.logo { left: 38px; }
  .placeholder.isbn { right: 18px; }

  /* Spine */
  .spine {
    width: 44px; height: 600px; background: var(--cover-blue-dark);
    display: flex; flex-direction: column; align-items: center; padding-top: 20px;
  }
  .spine .spine-title {
    writing-mode: vertical-rl; font-family: "Anton", Impact, sans-serif;
    font-size: 28px; color: var(--ink); letter-spacing: .5px;
  }
  .spine .spine-author {
    writing-mode: vertical-rl; font-family: "Roboto", Arial, sans-serif; font-weight: 700;
    font-size: 9px; color: var(--ink); margin-top: 60px; letter-spacing: .5px;
  }

  /* Front cover */
  .front-cover {
    width: 400px; height: 600px; background: var(--cover-blue); position: relative; overflow: hidden;
  }
  .cover-art {
    position: absolute; left: 0; right: 0; bottom: 0; height: 340px;
    background:
      radial-gradient(ellipse 60% 45% at 50% 85%, var(--rock) 0%, var(--rock-dark) 55%, transparent 75%),
      radial-gradient(ellipse 70% 40% at 55% 55%, rgba(255,255,255,.9) 0%, transparent 70%),
      linear-gradient(180deg, var(--cover-blue) 0%, var(--sky-top) 25%, var(--sky-mid) 60%, #c9c6c1 100%);
  }
  .front-title {
    position: absolute; left: 24px; top: 22px; right: 16px;
    font-family: "Anton", Impact, sans-serif; color: var(--ink);
    text-shadow: 2px 0 var(--outline), -2px 0 var(--outline), 0 2px var(--outline), 0 -2px var(--outline),
                 1.5px 1.5px var(--outline), -1.5px -1.5px var(--outline), 1.5px -1.5px var(--outline), -1.5px 1.5px var(--outline);
  }
  .front-title .author {
    position: absolute; right: 4px; top: 4px;
    font-family: "Roboto", Arial, sans-serif; font-weight: 900; font-size: 12px; text-shadow: none;
  }
  .front-title .initial {
    position: absolute; left: 0; top: 10px; font-size: 250px; line-height: 1;
  }
  .front-title .line-one {
    position: absolute; left: 100px; top: 30px; font-size: 96px; line-height: 1; white-space: nowrap;
  }
  .front-title .line-one .small-word { font-size: 40px; margin-left: 6px; }
  .front-title .subtitle {
    position: absolute; left: 102px; top: 148px; white-space: nowrap;
    font-family: "Roboto", Arial, sans-serif; font-weight: 900; font-size: 7.6px;
  }
  .front-title .line-two {
    position: absolute; left: 100px; top: 162px; font-size: 80px; line-height: 1; white-space: nowrap;
  }
</style>
</head>
<body>
  <div class="wrap">
    <section class="back-cover">
      <p class="author">TOMAS BRENHURST'S</p>
      <h2 class="title">STORM TO STILLNESS</h2>
      <p class="subtitle">FROM RIGID HABITS TO PIONEERS OF RENEWAL</p>
      <p class="blurb">Lorem ipsum dolor sit amet, consectetur adipisicing elit, sed do eiusmod tempor incididunt ut labore et dolore magna aliqua. Ut enim ad minim veniam, quis nostrud exercitation. Lorem ipsum dolor sit amet, consectetur adipisicing elit, sed do eiusmod tempor incididunt ut labore et dolore magna aliqua. Ut enim ad minim veniam, quis nostrud exercitation. Lorem ipsum dolor sit amet, consectetur adipisicing elit, sed do eiusmod tempor incididunt ut labore et dolore magna aliqua. Ut enim ad minim veniam, quis nostrud exercitation. Lorem ipsum dolor sit amet, consectetur adipisicing elit, sed do eiusmod tempor incididunt ut labore et dolore magna aliqua. Ut enim ad minim veniam, quis nostrud exercitation. Lorem ipsum dolor sit amet, consectetur adipisicing elit, sed do eiusmod tempor incididunt ut labore et dolore magna aliqua. Ut enim ad minim veniam, quis nostrud exercitation. Lorem ipsum dolor sit amet, consectetur adipisicing elit, sed do eiusmod tempor incididunt ut labore et dolore magna aliqua. Ut enim ad minim veniam, quis nostrud exercitation. Lorem ipsum dolor sit amet, consectetur adipisicing elit, sed do eiusmod tempor incididunt ut labore et dolore magna aliqua. Ut enim ad minim veniam, quis nostrud exercitation.</p>
      <div class="placeholder logo">LOGO</div>
      <div class="placeholder isbn">ISBN</div>
    </section>

    <section class="spine">
      <span class="spine-title">STORM TO STILLNESS</span>
      <span class="spine-author">TOMAS BRENHURST</span>
    </section>

    <section class="front-cover">
      <div class="cover-art" role="img" aria-label="Photo of three business people pulling a rope across a misty rocky mountain peak under a blue sky with clouds"></div>
      <h1 class="front-title">
        <span class="author">TOMAS BRENHURST'S</span>
        <span class="initial">S</span>
        <span class="line-one">TORM<span class="small-word">TO</span></span>
        <span class="subtitle">FROM RIGID HABITS TO PIONEERS OF RENEWAL</span>
        <span class="line-two">TILLNESS</span>
      </h1>
    </section>
  </div>
</body>
</html>
```